Redesign Quorvix.com Front Landing Page To Give It The Wow Factor Keeping SEO and Page Load Speeds

We need to redesign the landing page of www.quorvix.com to give it the wow factor

It must have exactly the same content, page size (currently 5.04 KB) or (5,156 bytes) and speed of the current site and rank 100/100 with Tallbeck.com tools as the page currently does.

This of course is subjective to content - in other words for an outstanding design - leeway will be given - THE WOW FACTOR IS CRITICAL.

THE PAGE MUST BE HTML5 COMPLIANT AND TOTALLY COMPLETE INCLUDING ANY SCRIPTS, CSS ETC, AND READY TO UPLOAD THE HTML PAGE AND CONTENT FOLDER TO THE SERVER WITH NO MODIFICATIONS REQUIRED.

SERVER IS CURRENTLY WINDOWS 2008 DATACENTER R2 BUT WILL SHORTLY BE UPGRADED TO WINDOWS 2012 DATACENTER R2 SERVER.

The current landing page loads faster that 96 % of the sites on the web according to Tallbeck Tools and that is on our current cable line connection that we are using while site is in development.

So we are looking for a fully optimized page that gives a outstanding first impression and SEO optimized.

It must be fully responsive for all screen size and utilize full page design on larger screen sizes.

The logo will remain to be strictly CSS and there are to be no images used on landing page other than the category link pages, all images must be fully optimized yet sharp and crisp.

A CSS content slider may be used to replace the Javascript rotator currently used - example www.vendrofade.com - we do have a licence for that slider

The winner will also be asked to look at the main script page and given priority in a contest for that as well.

Target Market(s)

World Online Trading Advertising and Business Directory Community Members

Industry/Entity Type

Seo

Requirements
Must have
• A feel of community - must be simple and clean.
• HTML5 Compliant
• Fully SEO optimized but not keyword spammed
• Keep the same content and links as existing landing page
• Search must be fully working and same as current options
Nice to have
• A WOW factor CSS slider - not bloated
Should not have
• No flash or any content that would slow down the front landing page Load Times

```html
<!DOCTYPE html>
<html lang="en">
<head>
<meta charset="utf-8">
<title>Quorvix – Online Trading, Classifieds &amp; Business Directory</title>
<link rel="stylesheet" href="https://fonts.googleapis.com/css2?family=Roboto:wght@300;400;500;700&display=swap">
<style>
:root{
  --orange:#e8501e;
  --blue:#2f8fdc;
  --blue-strip:#2e8de0;
  --text:#333;
  --light:#ececec;
  --line:#d6d6d6;
  --dark:#232323;
  --label:#d9431a;
}
*{box-sizing:border-box;margin:0;padding:0}
html,body{width:667px;height:1200px;overflow:hidden;background:#fff;font-family:"Roboto",Arial,sans-serif;color:var(--text)}
.page{position:relative;width:667px;height:1200px}
a{color:inherit;text-decoration:none}

/* top bar */
.topbar{position:absolute;left:0;top:0;width:667px;height:44px;background:#ebebeb}
.brand{position:absolute;left:53px;top:9px;font-size:24px;font-weight:700;color:var(--orange);letter-spacing:-.5px}
.util-nav{position:absolute;left:199px;top:20px;display:flex;gap:10px;font-size:6.4px;color:#666;text-transform:uppercase}
.region{position:absolute;left:524px;top:20px;font-size:6.6px;color:#777}
.region b{font-weight:400;color:#333}

/* main nav */
.mainnav{position:absolute;left:48px;top:47px;width:570px;height:35px;background:linear-gradient(#f0571f,#e2461a);display:flex}
.mainnav a{color:#fff;font-size:9px;line-height:35px;padding:0 13px;text-transform:uppercase}
.mainnav a.home{background:#2a2a2a;width:54px;padding:0;text-align:center}
.phone{position:absolute;left:510px;top:47px;width:108px;height:35px;background:var(--blue);color:#fff;font-size:11.5px;font-weight:500;display:flex;align-items:center;justify-content:center;gap:5px}

/* hero */
.hero{position:absolute;left:0;top:86px;width:667px;height:306px;
  background:
    radial-gradient(ellipse 120px 40px at 380px 210px,rgba(255,190,110,.35),rgba(255,190,110,0)),
    radial-gradient(ellipse 160px 50px at 560px 190px,rgba(255,200,130,.28),rgba(255,200,130,0)),
    radial-gradient(ellipse 140px 45px at 180px 200px,rgba(240,170,100,.25),rgba(240,170,100,0)),
    linear-gradient(90deg,rgba(20,24,30,.55) 0%,rgba(20,24,30,0) 14%,rgba(20,24,30,0) 86%,rgba(20,24,30,.35) 100%),
    linear-gradient(180deg,#2c3644 0%,#4a5565 18%,#6f747c 34%,#8a8580 46%,#5a5650 58%,#38383c 75%,#26272b 100%)}
.dots{position:absolute;left:645px;top:104px;display:flex;flex-direction:column;gap:4px}
.dots i{display:block;width:6px;height:6px;border-radius:50%;background:#fff}
.dots i.on{background:var(--blue)}
.search-panel{position:absolute;left:48px;top:248px;width:570px;height:144px;background:rgba(38,38,40,.9);border:1px solid #555}
.kw{position:absolute;left:43px;top:23px;width:238px;height:31px;background:#fff;border:1px solid #ccc;font-size:6.6px;color:#777;padding:12px 7px}
.in{position:absolute;left:289px;top:27px;color:#fff;font-size:12px;font-weight:700}
.cat{position:absolute;left:306px;top:23px;width:128px;height:31px;background:#fff;border:1px solid #ccc;font-size:6.6px;color:#777;padding:12px 7px}
.search-btn{position:absolute;left:446px;top:22px;width:76px;height:30px;background:linear-gradient(#3a9ae6,#2581cf);color:#fff;font-size:9.5px;font-weight:500;text-align:center;line-height:30px}
.opt{position:absolute;font-size:6.8px;color:#eee;display:flex;align-items:center;gap:3px}
.opt .box{width:7px;height:7px;background:#fff;border-radius:1px}
.opt .radio{width:7px;height:7px;background:#fff;border-radius:50%;border:2px solid #bbb}
.strip{position:absolute;left:0;bottom:0;width:568px;height:28px;background:var(--blue-strip);color:#fff;font-size:6.5px;text-align:center;line-height:28px}
.shadow{position:absolute;left:110px;top:392px;width:450px;height:14px;background:radial-gradient(ellipse at top,rgba(0,0,0,.22),rgba(0,0,0,0) 70%)}

/* sidebar */
.sidebar{position:absolute;left:47px;top:422px;width:143px;height:554px;border:1px solid var(--line);box-shadow:0 1px 2px rgba(0,0,0,.15)}
.sidebar h2{height:30px;background:var(--blue);color:#fff;font-size:8.6px;font-weight:400;line-height:30px;padding-left:18px}
.sidebar ul{list-style:none}
.sidebar li{height:24.3px;border-bottom:1px solid var(--line);font-size:8.4px;color:#333;display:flex;align-items:center;justify-content:space-between;padding:0 10px 0 13px}
.sidebar li:first-child{border-top:4px solid #fff;height:28px}
.sidebar li .chev{font-size:10px;color:#333}

/* categories */
.popular{position:absolute;left:204px;top:422px;width:412px;height:554px;border:1px solid var(--line)}
.popular h2{position:absolute;left:7px;top:10px;font-size:9.6px;font-weight:500;color:#222}
.popular h2 em{font-style:normal;color:var(--blue);font-weight:400}
.arrows{position:absolute;right:9px;top:7px;font-size:12px;color:#222;font-weight:700;letter-spacing:-1px}
.card{position:absolute;width:128px;height:164px;background:#fff;border:1px solid #ddd;box-shadow:0 1px 3px rgba(0,0,0,.18)}
.card .img{position:absolute;left:9px;top:6px;width:111px;height:118px;border:1px solid #e2e2e2;background:radial-gradient(circle,#fff 40%,#e6e6e6 100%)}
.card .label{position:absolute;left:0;top:137px;width:100%;text-align:center;font-size:7.2px;color:var(--label);text-transform:uppercase}
.img.antique{background:radial-gradient(ellipse 22px 36px at 50% 52%,#6b4526 0%,#a8774a 55%,rgba(168,119,74,0) 100%),radial-gradient(circle,#fff 45%,#e6e6e6 100%)}
.img.auto{background:radial-gradient(ellipse 48px 22px at 50% 52%,#8e9399 0%,#c9cdd1 55%,rgba(201,205,209,0) 100%),radial-gradient(circle,#fff 45%,#e6e6e6 100%)}
.img.boat{background:radial-gradient(ellipse 46px 22px at 50% 52%,#2a2f3a 0%,#e9ecef 55%,rgba(233,236,239,0) 100%),radial-gradient(circle,#fff 45%,#e6e6e6 100%)}
.img.b2b{background:radial-gradient(ellipse 48px 22px at 50% 50%,#c9302c 0%,#9aa0a6 45%,rgba(154,160,166,0) 100%),radial-gradient(circle,#fff 45%,#e6e6e6 100%)}
.img.dir{background:radial-gradient(circle 40px at 50% 48%,#e8502e 0%,#9b59b6 35%,#2f8fdc 60%,rgba(47,143,220,0) 100%),radial-gradient(circle,#fff 45%,#e6e6e6 100%)}
.img.net{background:radial-gradient(ellipse 50px 26px at 50% 52%,#2b3440 0%,#6da9e0 50%,rgba(109,169,224,0) 100%),radial-gradient(circle,#fff 45%,#e6e6e6 100%)}
.img.build{background:radial-gradient(ellipse 42px 32px at 50% 52%,#2a2a2a 0%,#e0a81e 55%,rgba(224,168,30,0) 100%),radial-gradient(circle,#fff 45%,#e6e6e6 100%)}
.img.deal{background:radial-gradient(ellipse 44px 38px at 50% 50%,#f07a1f 0%,#f5a623 45%,#3c9fd6 75%,rgba(60,159,214,0) 100%),radial-gradient(circle,#fff 45%,#e6e6e6 100%)}
.img.job{background:radial-gradient(ellipse 44px 34px at 50% 48%,#c8302a 0%,#d9d9d9 55%,rgba(217,217,217,0) 100%),radial-gradient(circle,#fff 45%,#e6e6e6 100%)}

/* footer */
.footer{position:absolute;left:0;top:1002px;width:667px;height:134px;background:var(--light)}
.fcol{position:absolute;top:0;height:134px}
.fcol h3{font-size:9px;font-weight:400;color:var(--blue);margin-top:22px;text-transform:uppercase}
.fcol p,.fcol li{font-size:7.2px;font-weight:400;color:#444;line-height:15.6px;list-style:none}
.divider{position:absolute;top:14px;width:1px;height:120px;background:#c9c9c9}
.email{margin-top:6px;width:109px;height:16px;background:#fff;border:1px solid #bbb;font-size:6px;color:#555;padding:4px 5px;position:relative}
.email:after{content:"";position:absolute;right:5px;top:4px;border-left:4px solid var(--blue);border-top:3px solid transparent;border-bottom:3px solid transparent}
.fb-brand{font-size:14px;font-weight:700;color:var(--orange);margin-top:22px}
.fb-count{font-size:4.6px;color:#555;margin-top:3px}
.fb-count b{color:var(--blue);font-weight:400}
.faces{display:grid;grid-template-columns:repeat(4,23px);gap:1px;margin-top:4px}
.faces i{display:block;height:23px;background:linear-gradient(135deg,#b9a8a0,#6d5a55)}
.faces i:nth-child(2n){background:linear-gradient(135deg,#c9c9d4,#8d8ea0)}
.faces i:nth-child(3n){background:linear-gradient(135deg,#d1b08a,#7a4e30)}
.plugin{font-size:4.6px;color:#777;margin-top:5px;display:flex;align-items:center;gap:2px;border-top:1px solid #ddd;padding-top:3px;width:95px}
.plugin i{display:inline-block;width:5px;height:5px;background:#3b5998}
.bottom{position:absolute;left:0;top:1142px;width:667px;height:58px;background:var(--dark)}
.copy{position:absolute;left:62px;top:24px;font-size:7px;color:#ddd}
.social{position:absolute;left:535px;top:21px;display:flex;gap:5px}
.social i{display:block;width:16px;height:16px;border-radius:2px}
.code{position:absolute;right:6px;bottom:6px;font-size:5.5px;color:#999}
</style>
</head>
<body>
<div class="page">

  <header class="topbar">
    <div class="brand">Quorvix</div>
    <nav class="util-nav">
      <a>Features</a><a>Map Listings</a><a>Post Free Ad</a><a>Post Free Auction</a><a>+ Search</a><a>Stores</a>
    </nav>
    <div class="region">All Regions : <b>United States</b> ⌄</div>
  </header>

  <nav class="mainnav">
    <a class="home">Home</a><a>About Us</a><a>Community</a><a>Help</a><a>Site Map</a><a>Contact Us</a>
  </nav>
  <div class="phone">
    <svg width="12" height="12" viewBox="0 0 12 12"><circle cx="6" cy="6" r="5.2" fill="none" stroke="#fff" stroke-width="1"/><path d="M4 3.3l1 1.2-.6.7c.4.9 1.1 1.6 2 2l.7-.6 1.2 1-.6.9c-2 .1-4.4-2.3-4.4-4.4z" fill="#fff"/></svg>
    1300 555 018
  </div>

  <section class="hero" role="img" aria-label="Dusk skyline of a city with high-rise towers and glowing lights">
    <div class="dots"><i class="on"></i><i></i><i></i><i></i></div>
  </section>

  <form class="search-panel">
    <div class="kw">WHAT ARE YOU LOOKING FOR ? Enter Keywords - Item</div>
    <div class="in">in</div>
    <div class="cat">All Categories</div>
    <div class="search-btn">SEARCH</div>
    <div class="opt" style="left:44px;top:72px">Search Titles <span class="box"></span></div>
    <div class="opt" style="left:153px;top:72px">Title &amp; Description <span class="box"></span></div>
    <div class="opt" style="left:281px;top:72px">Match Whole Words <span class="radio"></span></div>
    <div class="opt" style="left:414px;top:72px">Partial Word Match <span class="radio"></span></div>
    <div class="opt" style="left:44px;top:93px">Classifieds Only <span class="radio"></span></div>
    <div class="opt" style="left:167px;top:93px">Auctions Only <span class="radio"></span></div>
    <div class="opt" style="left:283px;top:93px">Auctions &amp; Classifieds <span class="radio"></span></div>
    <div class="opt" style="left:426px;top:93px">Buy Now Auctions <span class="radio"></span></div>
    <div class="strip">FEATURED LISTINGS &gt;&gt; GALLERY | GALLERY LIST | HOTTEST LISTINGSRECENT LISTINGS &gt;&gt; 24 HOURS &nbsp;| 1 WEEK | &nbsp;2 WEEKS | ALL NEW LISTINGS</div>
  </form>
  <div class="shadow"></div>

  <aside class="sidebar">
    <h2>ALL CATEGORIES LIST</h2>
    <ul>
      <li>Activities &amp; Events<span class="chev">»</span></li>
      <li>Antiques &amp; Collectables<span class="chev">»</span></li>
      <li>Automotive &amp; Vehicles<span class="chev">»</span></li>
      <li>Aviation &amp; Planes<span class="chev">»</span></li>
      <li>Boats &amp; Watercraft<span class="chev">»</span></li>
      <li>Business Directory<span class="chev">»</span></li>
      <li>Business to Business<span class="chev">»</span></li>
      <li>Charities &amp; Non Profits<span class="chev">»</span></li>
      <li>Clothing &amp; Accessories<span class="chev">»</span></li>
      <li>Computing &amp; Networking<span class="chev">»</span></li>
      <li>Construction &amp; Logging<span class="chev">»</span></li>
      <li>Daily Deals &amp; Services<span class="chev">»</span></li>
      <li>Dining-Food &amp; Beverages<span class="chev">»</span></li>
      <li>Education &amp; Training<span class="chev">»</span></li>
      <li>Electronics &amp; Phones<span class="chev">»</span></li>
      <li>Employment &amp; Careers<span class="chev">»</span></li>
      <li>Farming &amp; Agriculture<span class="chev">»</span></li>
      <li>Heavy Trucks &amp; Trailers<span class="chev">»</span></li>
      <li>Home &amp; Garden<span class="chev">»</span></li>
      <li>Industrial Machinery<span class="chev">»</span></li>
      <li>Jewelry &amp; Watches<span class="chev">»</span></li>
    </ul>
  </aside>

  <section class="popular">
    <h2>BROWSE OUR MOST <em>POPULAR CATEGORIES</em></h2>
    <div class="arrows">‹›</div>

    <div class="card" style="left:5px;top:32px"><div class="img antique" role="img" aria-label="Antique bronze urn"></div><div class="label">Antiques/Collectables</div></div>
    <div class="card" style="left:142px;top:32px"><div class="img auto" role="img" aria-label="Silver sedan car"></div><div class="label">Automotive &amp; Vehicles</div></div>
    <div class="card" style="left:279px;top:32px"><div class="img boat" role="img" aria-label="White motor yacht"></div><div class="label">Boats &amp; Watercraft</div></div>

    <div class="card" style="left:5px;top:207px"><div class="img b2b" role="img" aria-label="Letter dice spelling B2B"></div><div class="label">Business to Business</div></div>
    <div class="card" style="left:142px;top:207px"><div class="img dir" role="img" aria-label="Cluster of colourful business icons"></div><div class="label">Business Directory</div></div>
    <div class="card" style="left:279px;top:207px"><div class="img net" role="img" aria-label="Networked computers and devices"></div><div class="label">Computing &amp; Networking</div></div>

    <div class="card" style="left:5px;top:380px"><div class="img build" role="img" aria-label="Yellow log loader machine"></div><div class="label">Construction &amp; Logging</div></div>
    <div class="card" style="left:142px;top:380px"><div class="img deal" role="img" aria-label="Daily deal price tag"></div><div class="label">Daily Deals &amp; Services</div></div>
    <div class="card" style="left:279px;top:380px"><div class="img job" role="img" aria-label="Magnifier over job listings newspaper"></div><div class="label">Education &amp; Training</div></div>
  </section>

  <footer class="footer">
    <div class="fcol" style="left:56px;width:135px">
      <h3>Contact Us</h3>
      <p style="margin-top:6px;padding-left:2px">Lorem Ipsum has been the<br>standard dummy text ever since<br>when an unknown printer<br>Tel 010-5550142<br>Email hello@quorvix.com</p>
    </div>
    <div class="divider" style="left:196px"></div>
    <div class="fcol" style="left:214px">
      <h3>My Account</h3>
      <ul style="margin-top:7px"><li>Your Account</li><li>My orders</li><li>My credit slips</li><li>My addresses</li><li>Terms and conditions</li></ul>
    </div>
    <div class="divider" style="left:324px"></div>
    <div class="fcol" style="left:341px">
      <h3>News Letter</h3>
      <p style="margin-top:8px;font-size:6.6px">Sign Up for Our Newsletter:</p>
      <div class="email">Email</div>
    </div>
    <div class="divider" style="left:492px"></div>
    <div class="fcol" style="left:509px">
      <div class="fb-brand">Quorvix</div>
      <div class="fb-count">32,742 people like <b>Quorvix</b>.</div>
      <div class="faces"><i></i><i></i><i></i><i></i><i></i><i></i><i></i><i></i></div>
      <div class="plugin"><i></i>Social plugin</div>
    </div>
  </footer>

  <div class="bottom">
    <div class="copy">Copyright © 2015 &nbsp;All rights reserved.</div>
    <div class="social">
      <i style="background:#3fa9d8"></i><i style="background:#3b5a98"></i><i style="background:#3a6f8e"></i><i style="background:#7a6552"></i>
    </div>
    <div class="code">C6</div>
  </div>

</div>
</body>
</html>
```